STONE GATE WINE LABEL DESIGN PROJECT

We need an elegant wine label design for our new range of wine. We need 3 labels for the range

2015 STONE GATE SHIRAZ
2015 STONE GATE CABERNET SAUVIGNON
2015 STONE GATE CABERNET SHIRAZ

The Size is nominated at 120mm High x 90mm Wide (Front and Back) but we are open to creative expression even if size differs

We are open to any style of label and designer can work on their strengths. it can be modern/classic/old fashion etc

I have attached the stone gate logo ( the 2 olives) and a set up called wine mandatories which is in no way a design direction just the mandatory info that needs to appear on labels. The wine mandatories is just the information that needs to go on the label it has nothing to do with the design. DO not make designs based on this at all. These labels are for red wine not olive oil.

I have also attached some of the companies current olive oil labels ( KORVALE AND MERRIDOL AND STONE GATE so you can see other labels and how this wine product will sit in gift baskets.

Thanks
Tomas.

Reason: Hello Friends We have decided to extend the deadline to enable more submissions. Many of the designs submitted have images of olives and look like olive oil product. We only need the olive logo to be shown on the label but the rest of the design should be a classic simple red wine label. It is not olive oil or olive product - it is red wine. Please keep simple and stylish Thanks Tomas

Target Market(s)

35-65

Font styles to use
Serif

Requirements
Must have
• AS per brief
Nice to have
• as per brief
Should not have
• as per brief

```html
<!DOCTYPE html>
<html lang="en">
<head>
<meta charset="utf-8">
<title>Stone Gate Shiraz 2015 – Wine Label</title>
<link rel="stylesheet" href="https://fonts.googleapis.com/css2?family=Archivo:wght@800&family=Montserrat:wght@300;400;500&display=swap">
<style>
  :root {
    --page-bg: #f4f1f2;
    --label-black: #1d1d1d;
    --label-edge: #161616;
    --gold: #d98a1c;
    --gold-light: #e8a532;
    --text-light: #e9e6e2;
    --rule: #8a8a8a;
  }
  * { margin: 0; padding: 0; box-sizing: border-box; }
  html, body {
    width: 1200px;
    height: 1200px;
    overflow: hidden;
    background: var(--page-bg);
  }
  .canvas {
    position: relative;
    width: 1200px;
    height: 1200px;
    display: flex;
    align-items: center;
    justify-content: center;
  }
  .wine-label {
    position: relative;
    width: 620px;
    height: 1016px;
    background: linear-gradient(90deg, var(--label-edge) 0%, var(--label-black) 18%, var(--label-black) 82%, var(--label-edge) 100%);
    color: var(--text-light);
    font-family: "Montserrat", sans-serif;
    text-align: center;
  }
  .brand-mark {
    position: absolute;
    top: 88px;
    left: 0;
    right: 0;
    display: flex;
    flex-direction: column;
    align-items: center;
    gap: 22px;
  }
  .brand-mark__dot {
    width: 40px;
    height: 40px;
    border-radius: 50%;
    background: var(--gold);
  }
  .brand-mark__name {
    font-size: 17px;
    font-weight: 500;
    letter-spacing: 5px;
    color: var(--gold-light);
  }
  .wine-title {
    position: absolute;
    top: 300px;
    left: 0;
    right: 0;
    font-family: "Archivo", sans-serif;
    font-weight: 800;
    color: var(--gold);
    line-height: 1;
  }
  .wine-title__top {
    display: block;
    font-size: 128px;
    letter-spacing: 2px;
  }
  .wine-title__bottom {
    display: block;
    margin-top: 34px;
    font-size: 112px;
    letter-spacing: 8px;
  }
  .varietal {
    position: absolute;
    top: 750px;
    left: 50%;
    width: 190px;
    transform: translateX(-50%);
    border-top: 2px solid var(--rule);
    border-bottom: 2px solid var(--rule);
    padding: 20px 0 18px;
  }
  .varietal__name {
    display: block;
    font-size: 34px;
    font-weight: 400;
    letter-spacing: 10px;
    margin-right: -10px;
  }
  .varietal__year {
    display: block;
    margin-top: 10px;
    font-size: 25px;
    font-weight: 300;
    letter-spacing: 4px;
  }
  .mandatory {
    position: absolute;
    bottom: 40px;
    font-size: 22px;
    font-weight: 400;
    color: var(--gold-light);
    line-height: 1.2;
  }
  .mandatory--alcohol { left: 60px; text-align: left; }
  .mandatory--volume { right: 50px; text-align: right; }
</style>
</head>
<body>
  <main class="canvas">
    <section class="wine-label" aria-label="Stone Gate Shiraz 2015 front label">
      <div class="brand-mark">
        <span class="brand-mark__dot" aria-hidden="true"></span>
        <span class="brand-mark__name">THE STONE GATE.</span>
      </div>
      <h1 class="wine-title">
        <span class="wine-title__top">STONE</span>
        <span class="wine-title__bottom">GATE</span>
      </h1>
      <div class="varietal">
        <span class="varietal__name">SHIRAZ</span>
        <span class="varietal__year">2015</span>
      </div>
      <p class="mandatory mandatory--alcohol">14.0%<br>ALC/Vol</p>
      <p class="mandatory mandatory--volume">750 Ml</p>
    </section>
  </main>
</body>
</html>
```